Artistically challenged consultant needs a sexy business card.

I need a business card design for my consultancy business. I work primarily in the pacific on international development program focusing on tourism, economic empowerment and training. I would like to use a light blue/green to reference the pacific and also a simple design of a sprouting coconut (photo attached for reference) to reference growth and development.
The business card should have icons for email, phone, skype, ABN and linked in.

```html
<!DOCTYPE html>
<html lang="en">
<head>
<meta charset="UTF-8">
<title>Consultancy Business Card</title>
<link href="https://fonts.googleapis.com/css2?family=Open+Sans:wght@400;600&display=swap" rel="stylesheet">
<style>
  :root {
    --backdrop: #d9dde2;
    --card: #ffffff;
    --pacific-blue: #27a9e1;
    --reef-green: #00a651;
    --ink: #1a1a1a;
    --icon: #2a8fd0;
    --sprout-tone: #e3ead4;
    --husk-tone: #e6e0d3;
    --mark: #ebe7de;
  }
  * { margin: 0; padding: 0; box-sizing: border-box; }
  html, body {
    width: 1200px; height: 675px; overflow: hidden;
    background: var(--backdrop);
    font-family: "Open Sans", Arial, sans-serif;
  }
  .card {
    position: absolute; left: 100px; top: 60px;
    width: 1000px; height: 556px;
    background: var(--card);
    overflow: hidden;
    box-shadow: 0 10px 30px rgba(0,0,0,0.18);
  }
  .card__wave { position: absolute; left: 0; top: 0; width: 1000px; height: 556px; }
  .card__photo {
    position: absolute; left: 60px; top: 150px;
    width: 300px; height: 380px;
    border-radius: 12px;
    background: linear-gradient(180deg, var(--sprout-tone) 0%, var(--husk-tone) 100%);
  }
  .card__mark {
    position: absolute; left: 80px; top: 480px;
    width: 28px; height: 28px; border-radius: 50%;
    background: var(--mark);
  }
  .contact {
    position: absolute; left: 555px; top: 160px;
    list-style: none; color: var(--ink);
    font-size: 15px; letter-spacing: 0.5px; line-height: 1;
  }
  .contact__row { display: flex; align-items: center; height: 32px; white-space: nowrap; }
  .contact__row--plain { padding-left: 34px; }
  .contact__icon {
    width: 24px; height: 24px; margin-right: 10px; flex: none;
    border: 1.5px solid var(--icon); border-radius: 4px;
    display: flex; align-items: center; justify-content: center;
    color: var(--icon); font-size: 8px; font-weight: 600;
  }
  .contact__icon svg { width: 14px; height: 14px; }
</style>
</head>
<body>
  <div class="card">
    <svg class="card__wave" viewBox="0 0 1000 556" aria-hidden="true">
      <path d="M330 0 L1000 0 L1000 150 Q640 62 330 0 Z" fill="var(--pacific-blue)"/>
      <path d="M330 0 Q640 62 1000 150 L1000 188 Q660 88 330 0 Z" fill="var(--reef-green)"/>
    </svg>

    <div class="card__photo" role="img" aria-label="Faint photograph of a sprouting coconut with two young green leaves"></div>
    <div class="card__mark" aria-hidden="true"></div>

    <ul class="contact">
      <li class="contact__row contact__row--plain">xxxxxxxxxxxxxxxxxxxxxxx</li>
      <li class="contact__row contact__row--plain">xxxxx xxxxxxxxxxxxx</li>
      <li class="contact__row">
        <span class="contact__icon">
          <svg viewBox="0 0 24 24"><path fill="currentColor" d="M6.6 10.8a15 15 0 0 0 6.6 6.6l2.2-2.2c.3-.3.7-.4 1-.2 1.1.4 2.3.6 3.6.6.6 0 1 .4 1 1V20c0 .6-.4 1-1 1A17 17 0 0 1 3 4c0-.6.4-1 1-1h3.5c.6 0 1 .4 1 1 0 1.3.2 2.5.6 3.6.1.3 0 .7-.2 1z"/></svg>
        </span>xxxxxxxxxxxxxxxxxxxxxxxxxx
      </li>
      <li class="contact__row">
        <span class="contact__icon">
          <svg viewBox="0 0 24 24"><path fill="none" stroke="currentColor" stroke-width="2.4" stroke-linecap="round" d="M10 14a4 4 0 0 0 5.7 0l3-3a4 4 0 0 0-5.7-5.7l-1 1M14 10a4 4 0 0 0-5.7 0l-3 3a4 4 0 0 0 5.7 5.7l1-1"/></svg>
        </span>xxxxxx xxxxxxxxxxxxxx xxxxx
      </li>
      <li class="contact__row">
        <span class="contact__icon">
          <svg viewBox="0 0 24 24"><path fill="currentColor" d="M12 3 L12 16 L5 16 Z M13 6 L19 16 L13 16 Z M4 18 H20 L18 21 H6 Z"/></svg>
        </span>xxxxxx xxxxxxxxxxxxxxxx xxxxxx
      </li>
      <li class="contact__row">
        <span class="contact__icon">
          <svg viewBox="0 0 24 24"><path fill="currentColor" d="M4 4h16a1 1 0 0 1 1 1v11a1 1 0 0 1-1 1H9l-5 4v-4a1 1 0 0 1-1-1V5a1 1 0 0 1 1-1z"/></svg>
        </span>xxxxxxxxxxxxxxxxxxxx
      </li>
      <li class="contact__row">
        <span class="contact__icon">ABN</span>xxxxx xxxxxxxxxxxxx
      </li>
    </ul>
  </div>
</body>
</html>
```